Corporate Branding - Web and Print

A UK based company will like to use an existing logo to create branding materials for all marketing related documents, including business card, prints, letterhead, Website, Twitter, Facebook, Instagram logo etc. This company serves high-end clientele in the fashion, health and wellness and as such high quality and class is of utmost importance.
Where the logo can be modernised without losing its character then experiment. The main thing is to have a corporate branding which can be used later for brochures, Business Plan infographics.
The prominent colour within the organisation is burnt orange with no secondary colour. However if you believe a secondary colour is needed then use it, otherwise keep it simple and classy. Any chosen colours have to match perfectly.
Target Market(s)
High net worth individuals
Industry/Entity Type
Health And Wellness
Contact Information for Business Card
classy
Look and feel
Each slider illustrates characteristics of the customer's brand and the style your logo design should communicate.

```html
<!DOCTYPE html>
<html lang="en">
<head>
<meta charset="utf-8">
<title>Velora Business Card</title>
<link rel="stylesheet" href="https://fonts.googleapis.com/css2?family=Open+Sans:wght@400;600;700&display=swap">
<style>
  :root {
    --backdrop: #727371;
    --burnt-orange: #f7941e;
    --card-white: #ffffff;
    --ink: #111111;
    --muted: #7a7a7a;
  }
  * { margin: 0; padding: 0; box-sizing: border-box; }
  html, body {
    width: 848px;
    height: 1200px;
    overflow: hidden;
    background: var(--backdrop);
    font-family: "Open Sans", Arial, sans-serif;
  }
  .canvas { position: relative; width: 848px; height: 1200px; }

  .card { position: absolute; left: 120px; width: 610px; height: 367px; }
  .card-front {
    top: 175px;
    background: var(--burnt-orange);
    border-radius: 24px 0 24px 0;
  }
  .card-back {
    top: 651px;
    background: var(--card-white);
    border-radius: 0 24px 0 24px;
  }

  .front-brand {
    position: absolute;
    left: 0; right: 0; top: 150px;
    display: flex; align-items: center; justify-content: center; gap: 22px;
  }
  .front-brand .mark-dot {
    width: 70px; height: 70px; border-radius: 50%;
    background: var(--card-white);
  }
  .front-brand .brand-name {
    color: var(--card-white);
    font-weight: 700;
    font-size: 58px;
    letter-spacing: 2px;
    line-height: 1;
  }

  .back-brand {
    position: absolute; left: 0; right: 0; top: 42px;
    display: flex; flex-direction: column; align-items: center;
  }
  .back-brand .mark-dot {
    width: 62px; height: 62px; border-radius: 50%;
    background: var(--burnt-orange);
  }
  .back-brand .brand-name {
    margin-top: 10px;
    color: var(--burnt-orange);
    font-weight: 700;
    font-size: 42px;
    letter-spacing: 3px;
    line-height: 1;
  }

  .holder { position: absolute; left: 0; right: 0; top: 188px; text-align: center; }
  .holder-name { font-weight: 700; font-size: 22px; color: var(--ink); line-height: 30px; }
  .holder-title { font-size: 16px; color: var(--muted); line-height: 24px; }

  .contact {
    position: absolute;
    font-size: 12.5px;
    color: var(--ink);
    line-height: 18px;
  }
  .contact-row { display: flex; }
  .contact-row .label { width: 25px; }
  .contact-phone { left: 102px; top: 259px; }
  .contact-email { left: 102px; top: 312px; }
  .contact-address { left: 387px; top: 256px; }
  .contact-web { left: 387px; top: 310px; }
</style>
</head>
<body>
<main class="canvas">
  <section class="card card-front">
    <div class="front-brand">
      <span class="mark-dot"></span>
      <span class="brand-name">VELORA</span>
    </div>
  </section>

  <section class="card card-back">
    <div class="back-brand">
      <span class="mark-dot"></span>
      <span class="brand-name">VELORA</span>
    </div>

    <div class="holder">
      <p class="holder-name">Your Full Name</p>
      <p class="holder-title">Your Title</p>
    </div>

    <div class="contact contact-phone">
      <p class="contact-row"><span class="label">P</span><span>0100 555 0199</span></p>
      <p class="contact-row"><span class="label">M</span><span>+447700 90012</span></p>
    </div>
    <div class="contact contact-email">
      <p class="contact-row"><span class="label">E</span><span>youremail@velora.com</span></p>
    </div>
    <div class="contact contact-address">
      <p class="contact-row"><span class="label">A</span><span>Address Line 1</span></p>
      <p class="contact-row"><span class="label"></span><span>Address Line 2</span></p>
    </div>
    <div class="contact contact-web">
      <p class="contact-row"><span class="label">W</span><span>www.velora.com</span></p>
    </div>
  </section>
</main>
</body>
</html>
```